Retail Product Label Design

We need a 4" w X 3" h label. The label will be applied to a stand up zip lock clear poly bag. 2" at the bottom of the bag will remain clear as a window to the product. The product is small packs of minerals that are placed in fruit, vegetable and flower storage. please go to www.crispvelta.com for more info. We are thinking a green color with fruits and vegetables included similar to what we use now (see attached file). We would like to consider a retro-style (bright colors almost cartoonish like the labels on Tolmar's Alehall Beer Labels and glasses. We have exact specs for the layout when necessary. They can be found @ http://www.wrenfoldsupply.com/images/main/wfs-label-requirements.pdf. We would also like to freshen up our logo (see attached file). This will be one of possibly 3 labels. One label will focus on fruits and vegetables, one will focus on flowers and one will focus on valuables like electronics, cameras and silver jewelry. Colors should be limited to 5 or possibly 6.
Target Market(s)
Grocery store fruit and vegetable buyers
Industry/Entity Type
Electronics
Look and feel
Each slider illustrates characteristics of the customer's brand and the style your logo design should communicate.

```html
<!DOCTYPE html>
<html lang="en">
<head>
<meta charset="utf-8">
<title>CrispVelta – Fruit &amp; Vegetable Label</title>
<link rel="stylesheet" href="https://fonts.googleapis.com/css2?family=Dancing+Script:wght@700&family=Exo+2:wght@500;600&display=swap">
<style>
  :root {
    --page-bg: #ffffff;
    --lime: #c6dc2c;
    --lime-light: #e4f06a;
    --ring-white: #f6fbe6;
    --green-deep: #0d5f2a;
    --green-mid: #1f8a3f;
    --green-glow: #3aa655;
    --ink-white: #ffffff;
    --name-lime: #cfe436;
    --produce-orange: #f39a1e;
    --produce-red: #b8261f;
    --produce-green: #6a9a2a;
    --produce-gold: #e9c25a;
  }
  * { margin: 0; padding: 0; box-sizing: border-box; }
  html, body { width: 1200px; height: 900px; overflow: hidden; background: var(--page-bg); }
  .label {
    position: relative;
    width: 1200px;
    height: 900px;
    font-family: "Exo 2", sans-serif;
  }
  .label-shape { position: absolute; inset: 0; }
  .brand-crown-name {
    position: absolute;
    left: 0; width: 1200px;
    top: 212px;
    text-align: center;
    font-family: "Exo 2", sans-serif;
    font-weight: 600;
    font-size: 30px;
    color: var(--ink-white);
  }
  .produce-basket {
    position: absolute;
    left: 280px; top: 290px;
    width: 700px; height: 460px;
    border-radius: 48% 48% 42% 42% / 62% 62% 38% 38%;
    background:
      radial-gradient(circle at 30% 55%, var(--produce-red) 0 12%, transparent 30%),
      radial-gradient(circle at 62% 45%, var(--produce-orange) 0 14%, transparent 34%),
      radial-gradient(circle at 80% 75%, var(--produce-orange) 0 10%, transparent 26%),
      radial-gradient(circle at 55% 85%, var(--produce-green) 0 8%, transparent 22%),
      radial-gradient(circle at 50% 30%, var(--produce-gold) 0 18%, transparent 45%),
      linear-gradient(160deg, #c9893a, #a5452a 60%, #7a2a22);
    opacity: 0.95;
  }
  .tagline {
    position: absolute;
    font-family: "Dancing Script", cursive;
    font-weight: 700;
    color: var(--ink-white);
    -webkit-text-stroke: 3px var(--green-deep);
    paint-order: stroke fill;
    text-shadow: 2px 3px 4px rgba(0, 40, 10, 0.55);
    white-space: nowrap;
    transform-origin: center;
    letter-spacing: 3px;
  }
  .tagline-first {
    left: 120px; top: 420px;
    width: 1000px; text-align: center;
    font-size: 108px;
    transform: rotate(-20deg);
  }
  .tagline-second {
    left: 220px; top: 515px;
    width: 900px; text-align: center;
    font-size: 80px;
    transform: rotate(-20deg);
  }
  .brand-footer {
    position: absolute;
    left: 0; width: 1200px;
    top: 762px;
    text-align: center;
    font-family: "Exo 2", sans-serif;
    font-weight: 500;
    font-size: 34px;
    letter-spacing: 4px;
    color: var(--name-lime);
  }
</style>
</head>
<body>
<main class="label">
  <svg class="label-shape" width="1200" height="900" viewBox="0 0 1200 900" aria-hidden="true">
    <defs>
      <radialGradient id="panel-green" cx="50%" cy="42%" r="60%">
        <stop offset="0" stop-color="var(--green-glow)"/>
        <stop offset="0.55" stop-color="var(--green-mid)"/>
        <stop offset="1" stop-color="var(--green-deep)"/>
      </radialGradient>
    </defs>
    <!-- outer lime frame -->
    <path class="frame-outer" fill="var(--lime)"
      d="M60 215 Q300 125 600 125 Q900 125 1140 215 L1196 292 L1196 700 L1140 765 Q900 842 645 842 L600 892 L555 842 Q300 842 60 765 L4 700 L4 292 Z"/>
    <path class="frame-inner" fill="var(--ring-white)"
      d="M72 228 Q305 142 600 142 Q895 142 1128 228 L1180 300 L1180 692 L1128 750 Q895 826 600 826 Q305 826 72 750 L20 692 L20 300 Z"/>
    <!-- crown -->
    <g class="crown" fill="var(--lime)">
      <circle cx="600" cy="150" r="128"/>
      <circle cx="600" cy="28" r="36"/>
      <circle cx="535" cy="45" r="36"/>
      <circle cx="665" cy="45" r="36"/>
      <circle cx="485" cy="88" r="36"/>
      <circle cx="715" cy="88" r="36"/>
      <circle cx="462" cy="148" r="34"/>
      <circle cx="738" cy="148" r="34"/>
    </g>
    <circle class="crown-core" cx="600" cy="152" r="108" fill="var(--lime-light)"/>
    <!-- green panel -->
    <ellipse class="panel" cx="600" cy="490" rx="568" ry="330" fill="url(#panel-green)"/>
    <path class="panel-top" fill="url(#panel-green)"
      d="M470 200 Q600 150 730 200 L730 240 L470 240 Z"/>
    <circle class="brand-dot" cx="600" cy="150" r="42" fill="var(--ink-white)"/>
  </svg>

  <p class="brand-crown-name">CrispVelta</p>

  <div class="produce-basket" role="img" aria-label="Photo of a wicker basket filled with fresh fruit: grapes, apples, oranges, bananas, strawberries, cherries, kiwi and watermelon"></div>

  <p class="tagline tagline-first">with no special</p>
  <p class="tagline tagline-second">bags or containers</p>

  <p class="brand-footer">CrispVelta</p>
</main>
</body>
</html>
```